Brightstone Roofing Business Card

This is my current business card. But I’d like to make some changes. Somewhere on the card I’d like to list some of the services we offer. Maybe on the back? But I’d still like to keep the red. White and black modern look.

-residential & commercial roofing
-Roof Repairs & Maintenance
-Storm Damage & Insurance Claims specialist
-Christmas Lights and permanent Christmas lights
Fencing. Windows. Gutters. Siding. Sheetrock, painting.

```html
<!DOCTYPE html>
<html lang="en">
<head>
<meta charset="utf-8">
<title>Brightstone Roofing Business Card</title>
<link rel="stylesheet" href="https://fonts.googleapis.com/css2?family=Michroma&family=Poppins:wght@400;700&display=swap">
<style>
  :root {
    --stage: #9c9c9c;
    --white: #ffffff;
    --black: #000000;
    --ink: #1a1a1a;
    --red: #e30613;
    --band-dark: #8c0011;
    --band-bright: #d52b1e;
    --divider: #bdbdbd;
  }
  * { margin: 0; padding: 0; box-sizing: border-box; }
  html, body { width: 1093px; height: 1200px; overflow: hidden; }
  body { background: var(--stage); position: relative; font-family: "Poppins", sans-serif; }

  .card {
    position: absolute;
    left: 265px;
    width: 578px;
    height: 357px;
    border-radius: 24px;
    overflow: hidden;
  }
  .card--front { top: 226px; background: var(--white); color: var(--ink); }
  .card--back { top: 621px; background: var(--black); color: var(--white); }

  .band { position: absolute; left: 0; bottom: 0; width: 578px; height: 17px; display: block; }
  .band .dark { fill: var(--band-dark); }
  .band .bright { fill: var(--band-bright); }

  .brand { position: absolute; text-align: center; }
  .brand__disc { border-radius: 50%; background: var(--red); margin: 0 auto; }
  .brand__name {
    font-family: "Poppins", sans-serif;
    font-weight: 700;
    color: var(--red);
    line-height: 1.1;
    letter-spacing: 0.5px;
  }

  .card--front .brand { left: 20px; top: 100px; width: 252px; }
  .card--front .brand__disc { width: 98px; height: 98px; margin-bottom: 12px; position: absolute; left: 77px; top: 4px; }
  .card--front .brand__name { position: absolute; left: 0; top: 112px; width: 252px; font-size: 22px; }
  .card--front .brand__name span { display: block; font-size: 16px; }
  .card--front .brand { top: 100px; height: 160px; top: 52px; }

  .divider { position: absolute; left: 270px; top: 76px; width: 1px; height: 208px; background: var(--divider); }

  .person { position: absolute; left: 292px; top: 114px; }
  .person__name { font-family: "Michroma", sans-serif; font-size: 16px; font-weight: 400; letter-spacing: 0.5px; }
  .person__first { color: var(--red); }
  .person__last { color: var(--black); }
  .person__role { font-size: 15px; line-height: 20px; margin-top: 2px; }

  .contact { position: absolute; left: 292px; top: 177px; list-style: none; }
  .contact li { display: flex; align-items: center; gap: 7px; font-size: 17px; line-height: 21px; }
  .contact svg { width: 15px; height: 15px; flex: none; }

  .services { position: absolute; left: 31px; list-style: none; }
  .services li { display: flex; align-items: center; gap: 5px; font-size: 15px; line-height: 18.3px; }
  .services li::before {
    content: ""; width: 11px; height: 11px; border-radius: 50%;
    background: var(--red); flex: none;
  }
  .services--trades { top: 34px; }
  .services--roofing { top: 241px; }

  .card--back .brand { left: 320px; top: 32px; width: 242px; }
  .card--back .brand__disc { width: 118px; height: 118px; }
  .card--back .brand__name { margin-top: 18px; font-size: 26px; }
  .card--back .brand__name span { display: block; font-size: 20px; }
</style>
</head>
<body>

<section class="card card--front" aria-label="Business card front">
  <div class="brand">
    <div class="brand__disc"></div>
    <p class="brand__name">BRIGHTSTONE <span>ROOFING CO.</span></p>
  </div>

  <div class="divider"></div>

  <div class="person">
    <h1 class="person__name"><span class="person__first">DALE</span> <span class="person__last">MORROW</span></h1>
    <p class="person__role">OWNER</p>
  </div>

  <ul class="contact">
    <li>
      <svg viewBox="0 0 24 24" aria-hidden="true"><path fill="none" stroke="#e30613" stroke-width="2.4" stroke-linecap="round" stroke-linejoin="round" d="M6 3l3 4-2 2c1 2.5 3.5 5 6 6l2-2 4 3-2 3C9 19 5 15 3 6z M14 3a7 7 0 0 1 7 7 M14 7a3 3 0 0 1 3 3"/></svg>
      682-555-0148
    </li>
    <li>
      <svg viewBox="0 0 24 24" aria-hidden="true"><rect x="1" y="5" width="22" height="14" fill="#e30613"/><path d="M1 5l11 8 11-8M1 19l8-7M23 19l-8-7" fill="none" stroke="#ffffff" stroke-width="1.5"/></svg>
      dale@brightstoneroofing.co
    </li>
    <li>
      <svg viewBox="0 0 24 24" aria-hidden="true"><g fill="none" stroke="#e30613" stroke-width="2"><circle cx="12" cy="12" r="10"/><ellipse cx="12" cy="12" rx="4.5" ry="10"/><path d="M2 12h20M4 7h16M4 17h16"/></g></svg>
      www.brightstoneroofing.co
    </li>
  </ul>

  <svg class="band" viewBox="0 0 578 17" aria-hidden="true">
    <polygon class="dark" points="0,0 276,0 270,17 0,17"/>
    <polygon class="bright" points="282,0 578,0 578,17 276,17"/>
  </svg>
</section>

<section class="card card--back" aria-label="Business card back">
  <ul class="services services--trades">
    <li>Fencing</li>
    <li>Windows</li>
    <li>Gutters</li>
    <li>Siding</li>
    <li>Sheetrock</li>
    <li>Painting.</li>
  </ul>

  <div class="brand">
    <div class="brand__disc"></div>
    <p class="brand__name">BRIGHTSTONE <span>ROOFING CO.</span></p>
  </div>

  <ul class="services services--roofing">
    <li>Residential &amp; Commercial Roofing</li>
    <li>Roof Repairs &amp; Maintenance</li>
    <li>Storm Damage &amp; Insurance Claims Specialist</li>
    <li>Christmas Lights and Permanent Christmas Lights</li>
  </ul>

  <svg class="band" viewBox="0 0 578 17" aria-hidden="true">
    <polygon class="dark" points="0,0 278,0 272,17 0,17"/>
    <polygon class="bright" points="284,0 578,0 578,17 278,17"/>
  </svg>
</section>

</body>
</html>
```